Brindle Logistics Business Card Design

We are a trucking and warehousing company. We run freight in the US manly from the Pacific NW to TX and back up the the PNW. We also do warehousing where we store, move, and distribute freight. Looking for a clean and modern design of business card. We would like to look rich and elegant. Attached is our logo.

Industry/Entity Type

Trucking Company

Contact Information for Business Card

Looking for a clean and modern design of business card. We would like to look rich and elegant.

Font styles to use
Sans Serif

Colors

Designer to choose colors to be used in the design.

Requirements
Must have
• logo but it should not dominate the card
Should not have
• logo should not dominate the card

```html
<!DOCTYPE html>
<html lang="en">
<head>
<meta charset="utf-8">
<title>Brindle Logistics Business Card</title>
<link rel="stylesheet" href="https://fonts.googleapis.com/css2?family=Open+Sans:wght@400;600;700&display=swap">
<style>
  :root {
    --backdrop: #3a3330;
    --card: #161718;
    --card-edge: #232425;
    --ink: #ffffff;
    --muted: #9a9c9e;
    --brand-blue: #1f7fc4;
    --accent-orange: #f08a1c;
    --divider: #55585b;
  }
  * { box-sizing: border-box; margin: 0; padding: 0; }
  html, body { width: 1200px; height: 864px; overflow: hidden; }
  body {
    background: var(--backdrop);
    font-family: "Open Sans", Arial, sans-serif;
    position: relative;
  }
  .card {
    position: absolute;
    top: 282px;
    width: 520px;
    height: 300px;
    background: var(--card);
    border: 1px solid var(--card-edge);
    border-radius: 4px;
    box-shadow: 0 14px 30px rgba(0,0,0,.45);
    color: var(--ink);
  }
  .card--front { left: 50px; }
  .card--back { left: 630px; }

  .wordmark {
    display: flex;
    align-items: center;
    gap: 12px;
  }
  .wordmark__dot {
    width: 34px; height: 34px;
    border-radius: 50%;
    background: var(--brand-blue);
    flex: none;
  }
  .wordmark__name {
    font-weight: 600;
    font-size: 26px;
    line-height: 1.05;
    color: var(--ink);
    letter-spacing: .02em;
    text-transform: uppercase;
  }
  .card--front .wordmark {
    position: absolute;
    left: 95px; top: 100px;
  }
  .front__web {
    position: absolute;
    left: 0; right: 0; top: 200px;
    text-align: center;
    font-size: 13px;
    letter-spacing: .42em;
    color: var(--muted);
  }

  .card--back .wordmark {
    position: absolute;
    left: 26px; top: 114px;
  }
  .card--back .wordmark__name { font-size: 21px; }
  .back__divider {
    position: absolute;
    left: 285px; top: 62px;
    width: 1px; height: 180px;
    background: linear-gradient(var(--card), var(--divider) 25%, var(--divider) 75%, var(--card));
  }
  .contact {
    position: absolute;
    left: 300px; top: 72px;
    font-size: 12.5px;
    line-height: 1.4;
  }
  .contact__name {
    font-weight: 700;
    font-size: 16px;
    color: var(--brand-blue);
    text-transform: uppercase;
  }
  .contact__title {
    font-weight: 600;
    font-size: 12px;
    color: var(--accent-orange);
    text-transform: uppercase;
    margin-bottom: 8px;
  }
  .contact__address { margin-bottom: 2px; }
  .contact__list { list-style: none; }
  .contact__item { display: flex; align-items: center; gap: 8px; }
  .contact__icon { width: 11px; height: 11px; fill: var(--brand-blue); flex: none; }
  .contact__item--plain { padding-left: 19px; }
</style>
</head>
<body>
  <section class="card card--front" aria-label="Card front">
    <div class="wordmark">
      <span class="wordmark__dot"></span>
      <span class="wordmark__name">Brindle Logistics, LLC</span>
    </div>
    <p class="front__web">www.brindlelogistics.com</p>
  </section>

  <section class="card card--back" aria-label="Card back">
    <div class="wordmark">
      <span class="wordmark__dot"></span>
      <span class="wordmark__name">Brindle<br>Logistics, LLC</span>
    </div>
    <div class="back__divider"></div>
    <div class="contact">
      <p class="contact__name">Marcus Ellery</p>
      <p class="contact__title">President</p>
      <p class="contact__address">2170 Larchmont Avenue<br>Kent, WA 98032</p>
      <ul class="contact__list">
        <li class="contact__item">
          <svg class="contact__icon" viewBox="0 0 12 12"><path d="M2 1h3l1 3-1.5 1a6 6 0 0 0 2.5 2.5L8 6l3 1v3c0 .6-.4 1-1 1A9 9 0 0 1 1 2c0-.6.4-1 1-1z"/></svg>
          253 555 0148
        </li>
        <li class="contact__item">
          <svg class="contact__icon" viewBox="0 0 12 12"><path d="M3 0h6v12H3zM4 1.5v8h4v-8z"/></svg>
          253 555 0192
        </li>
        <li class="contact__item">
          <svg class="contact__icon" viewBox="0 0 12 12"><path d="M3 0h6v3H3zM1 4h10v5H9v3H3V9H1zM4 8v3h4V8z"/></svg>
          253 555 0173
        </li>
        <li class="contact__item">
          <svg class="contact__icon" viewBox="0 0 12 12"><path d="M0 2h12v8H0zM1 3l5 3.5L11 3z"/></svg>
          info@brindlelogistics.com
        </li>
        <li class="contact__item">
          <svg class="contact__icon" viewBox="0 0 12 12"><circle cx="6" cy="6" r="5.5"/></svg>
          www.brindlelogistics.com
        </li>
      </ul>
    </div>
  </section>
</body>
</html>
```